Brisk Mend's Blow Their Mind Website

We own a group of cell phone and tablet repair shops in the bay area that is emerging into the mobile device insurance industry and want to develop a site that is clean, organized, and efficient at communicating who we are, the services we provide and the positive feedback we have been getting from our clients. As we enter into this new field of business, Our goal is to attract larger corporate accounts.

We want our home screen to have a big focus on the protection plan for the devices right away much like the home screen from these links:

http://www.gadgetvault.com/

and also - https://us.keepitsnug.com/smartphone-protection.html

We also need to make our repair services clear, here is a website of a company that does repair and we want to highlight both ends of the business.

ww.fixnovo.com

So the home screen will include the tab categories at the top of the screen
home/ protection /repair /about /contact

The first portion will be protection and as you scroll down there will be the next section about repair and following that will be information about the company.

Target Market(s)

Individuals that would be looking for pricing, clients that come to our store, but ultimately the heavy hitters we would want to attract would be larger corporate accounts so the message we want to communicate is professional, organized and credible in the services we provide.

Industry/Entity Type

Cell Phone

Number of Pages Required

5+ page

Font styles to use
Serif

Colors
34a6d7

Requirements
Must have
• Eye catching, organized, with the wow factor that a business will look at our site and will be able to tell that we know what looks good and what grabs peoples attention. A large emphasis on the protection plan section like the links we provided and an organized home screen with the sections highlighted in the project description
• Tabs with links to different sections of the business such as protection that will go into detail about our protections plans and why our plan is best
• repair with a menu of the different prices we provide for different devices and services for that device
• an about us tab
• a contact us tab
Nice to have
• Artistic flow on the homescreen that the different sections flow together without looking too cookie cutter
• Wow factor
Should not have
• Clutter, confusion, disorganization, cheesy cookie cutter

```html
<!DOCTYPE html>
<html lang="en">
<head>
<meta charset="utf-8">
<title>Brisk Mend — Smartphone Protection &amp; Repair</title>
<link href="https://fonts.googleapis.com/css2?family=Open+Sans:wght@400;600;700&family=Roboto+Condensed:wght@300;400;700&display=swap" rel="stylesheet">
<style>
:root{
  --blue:#34a6d7;
  --blue-dark:#2a8fbb;
  --red:#e0204b;
  --navy:#0c1a33;
  --navy-2:#1b3560;
  --ink:#3d424c;
  --muted:#7b818b;
  --line:#e2e4e8;
  --paper:#ffffff;
  --mist:#f2f3f5;
  --bar:#50566a;
}
*{box-sizing:border-box;margin:0;padding:0}
html,body{width:1200px;height:3068px;overflow:hidden}
body{font-family:"Open Sans",Arial,sans-serif;color:var(--ink);background:var(--paper);position:relative}
.head{font-family:"Roboto Condensed","Arial Narrow",sans-serif}
section,header{position:absolute;left:0;width:1200px}
p{font-size:12px;line-height:1.6;color:var(--muted)}

/* header */
.site-header{top:0;height:100px;background:var(--paper)}
.brand{position:absolute;left:72px;top:18px;display:flex;align-items:center;gap:10px}
.brand-dot{width:30px;height:30px;border-radius:50%;background:var(--blue)}
.brand-name{font-size:24px;font-weight:600;color:var(--blue)}
.main-nav{position:absolute;left:620px;top:66px;width:360px;height:22px;background:var(--blue);display:flex;justify-content:space-around;align-items:center}
.main-nav a{color:#fff;text-decoration:none;font-size:10px;font-weight:700;letter-spacing:.5px}

/* hero */
.hero{top:100px;height:480px;background:linear-gradient(160deg,#1d3b6a 0%,var(--navy) 55%,#081226 100%);overflow:hidden}
.hero-copy{position:absolute;left:220px;top:40px;width:360px;z-index:1}
.hero-title{font-size:44px;line-height:1;font-weight:700;color:#fff;letter-spacing:1px}
.hero-title span{display:block;color:var(--blue);font-size:34px}
.hero-copy p{color:#c9d3e2;margin-top:22px;font-size:11px}
.hero-points{list-style:none;margin-top:24px}
.hero-points li{color:#e6ecf4;font-size:11px;margin-bottom:8px;padding-left:16px;position:relative}
.hero-points li::before{content:"";position:absolute;left:0;top:5px;width:6px;height:6px;background:var(--blue);border-radius:50%}
.hero-cta{display:inline-block;margin-top:44px;background:var(--red);color:#fff;padding:12px 26px;font-size:13px}
.hero-cta b{font-size:28px;font-family:"Roboto Condensed",sans-serif}
.hero-device{position:absolute;left:580px;top:30px;width:440px;height:440px;background:radial-gradient(ellipse at 50% 45%,#3c77ad 0%,#1a3a66 45%,rgba(12,26,51,0) 75%)}

/* features */
.features{top:580px;height:420px;background:var(--mist)}
.feature{position:absolute;width:320px;display:flex;gap:16px}
.feature svg{flex:none}
.feature h3{font-size:15px;font-weight:700;color:var(--ink);line-height:1.15;margin-bottom:8px}
.feature p{font-size:10px}
.f1{left:240px;top:60px}.f2{left:660px;top:60px}.f3{left:240px;top:240px}.f4{left:660px;top:240px}

/* pricing */
.pricing{top:1000px;height:460px;background:var(--paper)}
.pricing-band{position:absolute;left:0;top:48px;width:1200px;height:240px;background:linear-gradient(90deg,#20252e,#4c5868 50%,#20252e)}
.plans{position:absolute;left:300px;top:12px;display:flex;gap:20px}
.plan{width:190px;background:#fff;box-shadow:0 2px 6px rgba(0,0,0,.2);text-align:center}
.plan-name{background:#2b7fa9;color:#fff;font-size:10px;font-weight:700;padding:5px 0;letter-spacing:.5px}
.plan-top{background:var(--blue);height:90px;display:flex;align-items:center;justify-content:center}
.price{width:74px;height:74px;border:2px solid #fff;border-radius:50%;color:#fff;display:flex;flex-direction:column;justify-content:center}
.price b{font-family:"Roboto Condensed",sans-serif;font-size:24px}
.price small{font-size:8px}
.plan ul{list-style:none}
.plan li{font-size:10px;padding:7px 0;border-bottom:1px solid var(--line)}
.plan li.dim{color:#b5b9c0}
.plan-buy{display:block;background:var(--blue);color:#fff;font-size:11px;font-weight:700;padding:7px 0}
.plan.featured .plan-name{background:#b3173a}
.plan.featured .plan-top,.plan.featured .plan-buy{background:var(--red)}

/* difference */
.difference{top:1460px;height:300px}
.section-title{font-size:38px;font-weight:300;color:var(--ink);text-align:center;letter-spacing:1px}
.section-title em{font-style:normal;color:var(--red)}
.difference .section-title{margin-top:40px}
.diff-row{position:absolute;left:262px;display:flex;align-items:center;gap:24px}
.diff-bar{height:22px;background:var(--bar);color:#fff;font-size:10px;display:flex;align-items:center;padding-left:12px}
.d1{top:120px}.d2{top:172px}.d3{top:224px}

/* info blocks */
.info{height:440px}
.repair{top:1800px}
.brand-info{top:2280px}
.info-copy{position:absolute;left:260px;top:60px;width:400px;z-index:1}
.info-title{font-size:38px;font-weight:400;color:var(--ink);line-height:1.05;white-space:nowrap}
.info-title .red{color:var(--red)}
.info-title .blue{color:var(--blue)}
.info-copy p{margin-top:22px;font-size:11px}
.info-list{list-style:none;margin-top:22px}
.info-list li{font-size:11px;color:var(--muted);margin-bottom:6px;padding-left:18px;position:relative}
.info-list li::before{content:"";position:absolute;left:0;top:5px;width:7px;height:7px;border-radius:50%;background:var(--red)}
.brand-info .info-list li::before{background:var(--blue);border-radius:0;transform:rotate(45deg)}
.more{display:inline-block;margin-top:22px;border:1px solid var(--ink);font-size:10px;padding:6px 14px;color:var(--ink)}
.repair-art{position:absolute;left:700px;top:20px;width:500px;height:420px;background:linear-gradient(200deg,#7d828b 0%,#c8cbd0 45%,#ffffff 85%)}
.brand-art{position:absolute;left:880px;top:50px;width:260px;height:320px;background:radial-gradient(circle at 55% 45%,#8a8f98 0%,#c9ccd1 50%,#ffffff 80%)}

/* testimonials */
.testimonials{top:2752px;height:316px;background:linear-gradient(180deg,#56606e,#2c333d)}
.testimonials .section-title{color:#fff;margin-top:30px}
.quote{position:absolute;left:280px;top:120px;width:640px;height:160px;border:1px solid rgba(255,255,255,.5);background:rgba(255,255,255,.12);display:flex;gap:24px;padding:28px 32px}
.avatar{flex:none;width:70px;height:70px;border-radius:50%;background:#9aa3ae}
.quote p{color:#eef1f4;font-size:11px}
.quote cite{display:block;margin-top:12px;color:#fff;font-style:normal;font-size:11px;font-weight:700}
.arrow{position:absolute;top:180px}
.arrow.prev{left:232px}.arrow.next{left:938px}
</style>
</head>
<body>

<header class="site-header">
  <div class="brand"><span class="brand-dot"></span><span class="brand-name">Brisk Mend</span></div>
  <nav class="main-nav">
    <a href="#">HOME</a><a href="#">PROTECTION</a><a href="#">REPAIR</a><a href="#">ABOUT</a><a href="#">CONTACT</a>
  </nav>
</header>

<section class="hero">
  <div class="hero-copy">
    <h1 class="hero-title head">SMARTPHONE<span>PROTECTION PLAN</span></h1>
    <p>Whether your phone was bought new, used or refurbished, we cover it from the first day with a simple monthly plan and quick claims.</p>
    <ul class="hero-points">
      <li>Covers drops, spills and cracked screens</li>
      <li>Repair or replacement in one business day</li>
      <li>Unlimited claims with no hidden fees</li>
      <li>Low monthly deductibles for all devices</li>
    </ul>
    <div class="hero-cta">from <b>$ 5,99</b> a month</div>
  </div>
  <div class="hero-device" role="img" aria-label="Smartphone with a cracked screen splashing in water"></div>
</section>

<section class="features">
  <div class="feature f1">
    <svg width="44" height="44" viewBox="0 0 44 44"><rect x="4" y="8" width="36" height="32" fill="none" stroke="#3d424c" stroke-width="3"/><rect x="4" y="8" width="36" height="8" fill="#3d424c"/><g fill="#3d424c"><rect x="10" y="21" width="5" height="5"/><rect x="19" y="21" width="5" height="5"/><rect x="28" y="21" width="5" height="5"/><rect x="10" y="30" width="5" height="5"/><rect x="19" y="30" width="5" height="5"/></g></svg>
    <div><h3 class="head">NEXT-DAY CLAIMS<br>RESOLUTION</h3><p>Our claims team reviews every request within hours, so your repaired or replaced device reaches you by the next business day.</p></div>
  </div>
  <div class="feature f2">
    <svg width="44" height="44" viewBox="0 0 44 44"><path d="M22 4 C22 4 8 22 8 30 a14 14 0 0 0 28 0 C36 22 22 4 22 4z" fill="#8e4c8a"/></svg>
    <div><h3 class="head">NEXT-DAY CLAIMS<br>RESOLUTION</h3><p>Water damage is covered in full. Send in your phone and our technicians will dry, test and restore it to full working order.</p></div>
  </div>
  <div class="feature f3">
    <svg width="44" height="44" viewBox="0 0 44 44"><rect x="11" y="3" width="22" height="38" rx="3" fill="#2bb3a0"/><rect x="14" y="8" width="16" height="26" fill="#fff"/><path d="M16 14l12 8M26 12l-6 16" stroke="#2bb3a0" stroke-width="1.5"/></svg>
    <div><h3 class="head">NEXT-DAY CLAIMS<br>RESOLUTION</h3><p>Cracked screens are fixed with quality parts by certified technicians, and every repair comes with our own service warranty.</p></div>
  </div>
  <div class="feature f4">
    <svg width="44" height="44" viewBox="0 0 44 44"><circle cx="16" cy="24" r="9" fill="none" stroke="#34a6d7" stroke-width="5" stroke-dasharray="4 3"/><circle cx="16" cy="24" r="4" fill="#34a6d7"/><circle cx="32" cy="12" r="6" fill="none" stroke="#34a6d7" stroke-width="4" stroke-dasharray="3 2"/></svg>
    <div><h3 class="head">NEXT-DAY CLAIMS<br>RESOLUTION</h3><p>Mechanical failures outside warranty are handled too, from buttons and speakers to charging ports and batteries.</p></div>
  </div>
</section>

<section class="pricing">
  <div class="pricing-band" role="img" aria-label="Dark photo of a technician's workbench behind the plans"></div>
  <div class="plans">
    <div class="plan">
      <div class="plan-name">COMPANY 1</div>
      <div class="plan-top"><div class="price"><b>$8.50</b><small>/month</small></div></div>
      <ul><li>Accidental damage</li><li>Mechanical breakdown</li><li class="dim">Worldwide coverage</li><li>$100 deductible</li><li>$60 Subscriber</li><li>Screen damage fixed</li><li>2 Replacements per year</li><li>Cancel any time</li></ul>
      <span class="plan-buy">Buy Now</span>
    </div>
    <div class="plan">
      <div class="plan-name">COMPANY 1</div>
      <div class="plan-top"><div class="price"><b>$8.50</b><small>/month</small></div></div>
      <ul><li>Accidental damage</li><li>Mechanical breakdown</li><li class="dim">Worldwide coverage</li><li>$100 deductible</li><li>$60 Subscriber</li><li>Screen damage fixed</li><li>2 Replacements per year</li><li>Cancel any time</li></ul>
      <span class="plan-buy">Buy Now</span>
    </div>
    <div class="plan featured">
      <div class="plan-name">COMPANY 1</div>
      <div class="plan-top"><div class="price"><b>$6.50</b><small>/month</small></div></div>
      <ul><li>Accidental damage</li><li>Mechanical breakdown</li><li class="dim">Worldwide coverage</li><li>$100 deductible</li><li>$60 Subscriber</li><li>Screen damage fixed</li><li>2 Replacements per year</li><li>Cancel any time</li></ul>
      <span class="plan-buy">Buy Now</span>
    </div>
  </div>
</section>

<section class="difference">
  <h2 class="section-title head">WHAT MAKES US <em>DIFFERENT</em>?</h2>
  <div class="diff-row d1">
    <svg width="30" height="30" viewBox="0 0 30 30"><circle cx="15" cy="15" r="12" fill="none" stroke="#7b818b" stroke-width="2.5"/><path d="M15 8v8h6" fill="none" stroke="#7b818b" stroke-width="2.5"/></svg>
    <div class="diff-bar" style="width:680px">Most claims are resolved within a single business day, straight to your door</div>
  </div>
  <div class="diff-row d2">
    <svg width="30" height="30" viewBox="0 0 30 30"><rect x="3" y="5" width="24" height="20" fill="none" stroke="#7b818b" stroke-width="2.5"/><path d="M3 11h24" stroke="#7b818b" stroke-width="2.5"/></svg>
    <div class="diff-bar" style="width:600px">Our own repair shops across the bay area, staffed by certified technicians</div>
  </div>
  <div class="diff-row d3">
    <svg width="30" height="30" viewBox="0 0 30 30"><path d="M3 12L15 4l12 8v2H3z" fill="#7b818b"/><g fill="#7b818b"><rect x="6" y="15" width="3" height="9"/><rect x="13.5" y="15" width="3" height="9"/><rect x="21" y="15" width="3" height="9"/><rect x="3" y="25" width="24" height="3"/></g></svg>
    <div class="diff-bar" style="width:480px">Plans built for individuals and corporate fleets</div>
  </div>
</section>

<section class="info repair">
  <div class="repair-art" role="img" aria-label="Shards of shattered glass bursting outward"></div>
  <div class="info-copy">
    <h2 class="info-title head"><span class="red">REPAIR</span> INFORMATION</h2>
    <p>We fix phones and tablets of every make, from cracked glass and tired batteries to water damage and broken ports. Every repair uses quality parts and is tested before it goes back to you.</p>
    <ul class="info-list"><li>Screen replacement</li><li>Battery service</li><li>Water damage</li><li>Charging ports</li></ul>
    <span class="more">Read more</span>
  </div>
</section>

<section class="info brand-info">
  <div class="brand-art" role="img" aria-label="Grey illustration of a phone with a repair tool"></div>
  <div class="info-copy">
    <h2 class="info-title head"><span class="blue">BRISK MEND</span><br>INFORMATION</h2>
    <p>Brisk Mend began as a small group of repair shops and now protects thousands of devices for families and businesses, with the same care behind every claim and every repair.</p>
    <ul class="info-list"><li>Founded in the bay area</li><li>Certified technicians</li><li>Corporate accounts</li><li>Friendly local stores</li></ul>
    <span class="more">Read more</span>
  </div>
</section>

<section class="testimonials" role="region" aria-label="Client testimonials">
  <h2 class="section-title head">WHAT OUR <em>CLIENTS</em> SAY</h2>
  <svg class="arrow prev" width="24" height="40" viewBox="0 0 24 40"><path d="M18 4L6 20l12 16" fill="none" stroke="#fff" stroke-width="3"/></svg>
  <div class="quote">
    <div class="avatar" role="img" aria-label="Client portrait"></div>
    <div>
      <p>My screen was fixed the very next day and the whole claim took five minutes. The staff were friendly, clear about the price and quick to help. I have since moved our whole office fleet over to their plan.</p>
      <cite>Happy Client</cite>
    </div>
  </div>
  <svg class="arrow next" width="24" height="40" viewBox="0 0 24 40"><path d="M6 4l12 16L6 36" fill="none" stroke="#fff" stroke-width="3"/></svg>
</section>

</body>
</html>
```